Business Card Design Project

Need a business card for a web application development company based in Denver Colorado. Our tagline is "Growing Your Brand, Not Just a Home Page"

Double-sided design with logo, taglin on one side and contact details on other (+ any other design elements).

Can use either or both of our logos (both are attached to project in psd and eps format)

Industry/Entity Type

Business

Requirements
Must have
• Use blue and gray as the main color. Something similar to the color scheme of the home page of our web site (www.northgate-pixel-foundry.com)

```html
<!DOCTYPE html>
<html lang="en">
<head>
<meta charset="utf-8">
<title>Northgate Pixel Foundry — Business Cards</title>
<link rel="stylesheet" href="https://fonts.googleapis.com/css2?family=Cabin+Condensed:wght@400;600&display=swap">
<style>
  :root {
    --bg: #e6e8ec;
    --card: #f7f8fa;
    --card-shade: #e9ebef;
    --blue: #4a5a8c;
    --gray: #b9bec8;
    --white: #ffffff;
  }
  * { margin: 0; padding: 0; box-sizing: border-box; }
  html, body {
    width: 1200px; height: 900px; overflow: hidden;
    background: var(--bg);
    font-family: "Cabin Condensed", sans-serif;
  }
  .canvas {
    width: 1200px; height: 900px;
    display: flex; flex-direction: column; align-items: center; justify-content: center;
    gap: 56px;
  }
  .card {
    position: relative;
    width: 640px; height: 366px;
    background: linear-gradient(135deg, var(--white), var(--card) 60%, var(--card-shade));
    box-shadow: 0 10px 28px rgba(40, 50, 80, 0.18);
    overflow: hidden;
  }

  /* Contact side */
  .contact-band {
    position: absolute; inset: 0;
    background: var(--blue);
    clip-path: polygon(0 0, 46% 0, 64% 100%, 0 100%);
  }
  .brand-name {
    position: absolute; right: 28px; top: 24px;
    font-weight: 600; font-size: 22px; line-height: 1;
    color: var(--blue); letter-spacing: 0.5px; text-transform: uppercase;
  }
  .address {
    position: absolute; left: 30px; top: 30px;
    font-style: normal;
    color: var(--white); font-size: 27px; line-height: 1.08;
  }
  .person-name {
    position: absolute; right: 48px; top: 130px;
    color: var(--blue); font-size: 42px;
  }
  .phone {
    position: absolute; right: 30px; top: 250px;
    color: var(--blue); font-size: 21px;
  }
  .web-lines {
    position: absolute; left: 30px; bottom: 24px;
    color: var(--white); font-size: 19px; line-height: 1.35;
  }

  /* Tagline side */
  .frame {
    position: absolute; inset: 22px;
    border: 6px solid var(--blue);
    box-shadow: inset 0 0 0 2px var(--gray), 0 0 0 2px var(--gray);
  }
  .logo-lockup {
    position: absolute; left: 0; right: 0; top: 110px;
    display: flex; align-items: center; justify-content: center; gap: 14px;
  }
  .logo-dot {
    width: 22px; height: 22px; border-radius: 50%; background: var(--blue);
  }
  .logo-name {
    font-weight: 600; font-size: 38px; line-height: 1;
    color: var(--blue); text-transform: uppercase; letter-spacing: 1px;
  }
  .tagline-rule {
    position: absolute; left: 80px; right: 80px; top: 208px;
    height: 2px; background: var(--blue);
  }
  .tagline {
    position: absolute; left: 0; right: 0; top: 222px;
    text-align: center; color: var(--blue); font-size: 33px;
  }
</style>
</head>
<body>
<main class="canvas">
  <section class="card card-contact">
    <div class="contact-band"></div>
    <div class="brand-name">Northgate Pixel Foundry</div>
    <address class="address">4200 Larkspur Circle<br>Suite #260<br>Millbrook<br>NV 89415</address>
    <div class="person-name">Jordan Vale</div>
    <div class="phone">Phone: (555) 014-2290</div>
    <div class="web-lines">www.northgate-pixel-foundry.com<br>Email: info@northgate-pixel-foundry.com</div>
  </section>

  <section class="card card-tagline">
    <div class="frame"></div>
    <div class="logo-lockup">
      <span class="logo-dot"></span>
      <span class="logo-name">Northgate Pixel Foundry</span>
    </div>
    <div class="tagline-rule"></div>
    <p class="tagline">Growing Your Brand, Not Just a Home Page</p>
  </section>
</main>
</body>
</html>
```